Business Cards

Business cards (double-sided) to be handed out to clients and potential clients, with contact details, logo .

Target Market(s)

Small to medium size businesses

Industry/Entity Type

Accountants

Contact Information for Business Card

Brightwater Ledger & Counsel Ltd

Colors

Designer to choose only greyscale colors for use in the design.

Requirements
Must have
• Name, Title, Address, Phone number, Email, Website
Nice to have
• Modern, clean lines, classy
Should not have
• Business cards to be double-sided. Form keeps reverting to single-sided.

```html
<!DOCTYPE html>
<html lang="en">
<head>
<meta charset="utf-8">
<title>Brightwater Ledger &amp; Counsel – Business Cards</title>
<link href="https://fonts.googleapis.com/css2?family=Josefin+Sans:wght@400&family=Montserrat:wght@400;700&display=swap" rel="stylesheet">
<style>
  :root {
    --backdrop: #e8e6e2;
    --card: #ffffff;
    --ink: #111111;
    --ink-soft: #3a3a3a;
    --title: #1c1c3a;
    --shadow: rgba(0, 0, 0, 0.28);
  }
  * { box-sizing: border-box; margin: 0; padding: 0; }
  html, body {
    width: 1200px; height: 1200px; overflow: hidden;
    background: var(--backdrop);
  }
  .canvas { position: relative; width: 1200px; height: 1200px; }
  .card {
    position: absolute; left: 222px; width: 756px; height: 432px;
    background: var(--card); border-radius: 34px;
    box-shadow: 6px 8px 14px var(--shadow);
  }
  .card--front { top: 156px; }
  .card--back { top: 612px; }

  .wordmark {
    position: absolute; font-family: "Josefin Sans", sans-serif;
    font-weight: 400; color: var(--ink); text-transform: uppercase;
    text-align: center; line-height: 1;
  }
  .wordmark__main { display: block; }
  .wordmark__sub { display: block; }

  .card--front .wordmark { left: 52px; width: 296px; top: 182px; }
  .card--front .wordmark__main { font-size: 36px; letter-spacing: 3px; }
  .card--front .wordmark__sub { font-size: 12.5px; letter-spacing: 3.2px; margin-top: 12px; }

  .card--back .wordmark { left: 0; width: 756px; top: 152px; }
  .card--back .wordmark__main { font-size: 76px; letter-spacing: 7px; }
  .card--back .wordmark__sub { font-size: 21px; letter-spacing: 6.5px; margin-top: 22px; }

  .divider {
    position: absolute; left: 377px; top: 97px; width: 2px; height: 238px;
    background: var(--ink);
  }
  .details {
    position: absolute; left: 405px; top: 96px;
    font-family: "Montserrat", sans-serif; color: var(--ink-soft);
  }
  .details__name { font-weight: 700; font-size: 27px; color: var(--ink); line-height: 1.1; }
  .details__title { font-size: 16.5px; color: var(--title); margin-top: 2px; }
  .details__address { font-size: 18.5px; line-height: 27px; margin-top: 18px; }
  .contact-list { list-style: none; margin-top: 12px; }
  .contact-list li {
    display: flex; align-items: center; gap: 6px;
    font-size: 18.5px; line-height: 27px;
  }
  .contact-list svg { width: 17px; height: 17px; fill: var(--ink); flex: none; }
</style>
</head>
<body>
<main class="canvas">
  <section class="card card--front" aria-label="Card front">
    <div class="wordmark">
      <span class="wordmark__main">Brightwater</span>
      <span class="wordmark__sub">Ledger &amp; Counsel</span>
    </div>
    <div class="divider"></div>
    <div class="details">
      <p class="details__name">DANIEL MOREAU</p>
      <p class="details__title">Owner/Ceo</p>
      <p class="details__address">1850 Harbor Crest Lane<br>Bayview CA 90000</p>
      <ul class="contact-list">
        <li><svg viewBox="0 0 24 24" aria-hidden="true"><path d="M6.6 10.8a15.1 15.1 0 0 0 6.6 6.6l2.2-2.2c.3-.3.7-.4 1-.2 1.1.4 2.3.6 3.6.6.6 0 1 .4 1 1V20c0 .6-.4 1-1 1A17 17 0 0 1 3 4c0-.6.4-1 1-1h3.5c.6 0 1 .4 1 1 0 1.3.2 2.5.6 3.6.1.3 0 .7-.2 1z"/></svg>123 456 789</li>
        <li><svg viewBox="0 0 24 24" aria-hidden="true"><path d="M7 1h10a2 2 0 0 1 2 2v18a2 2 0 0 1-2 2H7a2 2 0 0 1-2-2V3a2 2 0 0 1 2-2zm0 3v15h10V4zm5 16.2a1 1 0 1 0 0 1.6 1 1 0 0 0 0-1.6z"/></svg>123 456 789</li>
        <li><svg viewBox="0 0 24 24" aria-hidden="true"><path d="M2 5h20v2l-10 6L2 7zm0 4.3 10 6 10-6V19H2z"/></svg>info@yourgmail.com</li>
        <li><svg viewBox="0 0 24 24" aria-hidden="true"><path d="M12 2a10 10 0 1 0 0 20 10 10 0 0 0 0-20zm6.9 6h-3a15 15 0 0 0-1.3-3.9A8 8 0 0 1 18.9 8zM12 4c.9 1.2 1.6 2.6 2 4h-4c.4-1.4 1.1-2.8 2-4zM4.3 14a8 8 0 0 1 0-4h3.4a16 16 0 0 0 0 4zm.8 2h3a15 15 0 0 0 1.3 3.9A8 8 0 0 1 5.1 16zm3-8h-3a8 8 0 0 1 4.3-3.9A15 15 0 0 0 8.1 8zM12 20c-.9-1.2-1.6-2.6-2-4h4c-.4 1.4-1.1 2.8-2 4zm2.3-6H9.7a14 14 0 0 1 0-4h4.6a14 14 0 0 1 0 4zm.3 5.9A15 15 0 0 0 15.9 16h3a8 8 0 0 1-4.3 3.9zm1.7-5.9a16 16 0 0 0 0-4h3.4a8 8 0 0 1 0 4z"/></svg>www.yourwebsite.com</li>
      </ul>
    </div>
  </section>

  <section class="card card--back" aria-label="Card back">
    <div class="wordmark">
      <span class="wordmark__main">Brightwater</span>
      <span class="wordmark__sub">Ledger &amp; Counsel</span>
    </div>
  </section>
</main>
</body>
</html>
```